Muddy Boots Pet Parlour

Design a flyer (A5 - I think!) with bright colours to promote an in home Dog Service.
Include an animated picture of a dog (being walked/playing/jumping etc)
Bold Heading, list of services with animated pictures, contact details

• Add price list to back of A5 Flyer with same colours and design as front page of flyer - See Attached.

```html
<!DOCTYPE html>
<html lang="en">
<head>
<meta charset="utf-8">
<title>Muddy Boots Pet Parlour – Flyer</title>
<link rel="stylesheet" href="https://fonts.googleapis.com/css2?family=Arimo:wght@400;700&family=Comic+Neue:wght@400;700&display=swap">
<style>
  :root {
    --orange: #f47b20;
    --orange-dark: #e0650a;
    --green: #1ec35c;
    --green-band: #1a8a3f;
    --purple: #663f86;
    --grey-band: #e6e6e6;
    --ink: #111;
    --white: #fff;
    --stage: #1e1e1e;
  }
  * { box-sizing: border-box; margin: 0; padding: 0; }
  html, body { width: 902px; height: 1200px; overflow: hidden; }
  body { background: var(--stage); position: relative; font-family: "Arimo", Arial, sans-serif; }

  .flyer {
    position: absolute; left: 81px; top: 81px;
    width: 740px; height: 1038px;
    background: var(--white); overflow: hidden;
  }
  .flyer-header {
    height: 215px;
    background: linear-gradient(90deg, var(--orange-dark), #ff8a1a 55%, var(--orange-dark));
    display: flex; align-items: center; justify-content: center;
  }
  .flyer-title {
    color: var(--white); font-weight: 700; font-size: 66px; line-height: 1.12;
    text-align: center; letter-spacing: 0.5px;
  }

  .services {
    position: absolute; left: 27px; top: 230px; width: 534px; height: 560px;
    background: var(--purple); border-radius: 24px; padding: 20px 10px 0 26px;
  }
  .service { margin-bottom: 20px; }
  .service-q {
    font-weight: 700; font-size: 22.5px; line-height: 1.15; text-transform: uppercase;
  }
  .service-q.is-orange { color: var(--orange); }
  .service-q.is-green { color: var(--green); }
  .service-a {
    font-family: "Comic Neue", "Comic Sans MS", cursive; color: var(--white);
    font-size: 18.5px; line-height: 1.3; margin-top: 6px; padding-left: 18px; text-indent: -14px;
  }

  .paw { position: absolute; border-radius: 40%; }
  .paw-green { left: 611px; top: 262px; width: 94px; height: 86px; background: var(--green); }
  .paw-orange { left: 580px; top: 416px; width: 78px; height: 74px; background: var(--orange); }
  .paw-purple { left: 631px; top: 554px; width: 72px; height: 68px; background: var(--purple); }

  .contact-band {
    position: absolute; left: 0; top: 802px; width: 740px; height: 135px;
    background: var(--grey-band); padding: 18px 0 0 42px;
  }
  .contact-lead { font-size: 15.5px; font-weight: 700; color: var(--ink); }
  .contact-call { font-size: 27px; color: var(--ink); margin-top: 8px; }
  .contact-call .phone { color: var(--green-band); font-weight: 700; }
  .contact-slogan { font-size: 31px; font-weight: 700; color: var(--orange); margin-top: 6px; }

  .footer-band {
    position: absolute; left: 0; top: 950px; width: 740px; height: 88px;
    background: var(--green-band); display: flex; align-items: center; padding-left: 34px;
  }
  .web { color: var(--white); font-size: 32px; }

  .photo {
    position: absolute; border-radius: 50%;
    border: 6px solid var(--orange); box-shadow: 0 0 0 4px var(--white), 0 4px 10px rgba(0,0,0,.25);
  }
  .photo-play { left: 404px; top: 661px; width: 172px; height: 172px;
    background: radial-gradient(circle at 45% 40%, #6b5a4a, #4f7a45 70%, #8ea86d); }
  .photo-bath { left: 582px; top: 672px; width: 140px; height: 140px;
    background: radial-gradient(circle at 50% 50%, #d8a265, #f0e0cc 75%); }
  .photo-puppy { left: 516px; top: 794px; width: 208px; height: 208px;
    background: radial-gradient(circle at 50% 45%, #c99a6a, #e8e2dc 60%, #b58b5c); }
</style>
</head>
<body>
  <main class="flyer">
    <header class="flyer-header">
      <h1 class="flyer-title">Muddy Boots<br>Pet Parlour</h1>
    </header>

    <section class="services">
      <div class="service">
        <p class="service-q is-orange">Tired of picking up dog poop?</p>
        <p class="service-a">- arrange for us to do it for you!</p>
      </div>
      <div class="service">
        <p class="service-q is-green">Need a break from walking the dog?</p>
        <p class="service-a">- we will come and collect your dog and take it for a walk!</p>
      </div>
      <div class="service">
        <p class="service-q is-orange">Can’t get home in time to feed your dog?</p>
        <p class="service-a">- use our dog feeding service!</p>
      </div>
      <div class="service">
        <p class="service-q is-green">Want someone to play with your dog while you’re at work?</p>
        <p class="service-a">- we will be Muddy Boots Pet Parlour!</p>
      </div>
      <div class="service">
        <p class="service-q is-orange">Dog needs a bath?</p>
        <p class="service-a">- we’ll arrange for a professional to keep it clean!</p>
      </div>
    </section>

    <div class="paw paw-green" role="img" aria-label="Green paw print"></div>
    <div class="paw paw-orange" role="img" aria-label="Orange paw print"></div>
    <div class="paw paw-purple" role="img" aria-label="Purple paw print"></div>

    <section class="contact-band">
      <p class="contact-lead">FOR ALL SERVICES RELATED TO YOUR DOG</p>
      <p class="contact-call">CALL MBPP @ <span class="phone">0400 123 987</span></p>
      <p class="contact-slogan">“Muddy Boots Pet Parlour”</p>
    </section>

    <footer class="footer-band">
      <p class="web">www.muddybootspetparlour.com.au</p>
    </footer>

    <div class="photo photo-play" role="img" aria-label="Photo of a dog leaping to catch a frisbee on grass"></div>
    <div class="photo photo-bath" role="img" aria-label="Photo of a golden dog being shampooed"></div>
    <div class="photo photo-puppy" role="img" aria-label="Photo of a small puppy in a basket"></div>
  </main>
</body>
</html>
```